Lumo4Kart - a fintech company - business card

We need a business card design for our Payments Technology company in Sydney, Australia. We provide business with payment solutions expanding across EFTPOS machines, online payment gateways and mobile payment solutions. We would like to see designs that are clean, classy and professional.
Target Market(s)
Business professionals, executives, c-suite
Industry/Entity Type
Fintech
Contact Information for Business Card
Will be on 400gsm. Logo will most likely be spot gloss unless designer recommends otherwise.
Font styles to use
Sans Serif
Requirements
Must have
- We need our website (lumo4kart.com.au), email (contact@lumo4kart.com.au), mobile (0432 587 904) and direct phone number (02 6815 3927) to feature on the card along with our logo (attached) and the words "EFTPOS | ONLINE | MOBILE"
- Font = Roboto

```html
<!DOCTYPE html>
<html lang="en">
<head>
<meta charset="utf-8">
<title>Lumo4Kart business card</title>
<link rel="stylesheet" href="https://fonts.googleapis.com/css2?family=Roboto:wght@700;900&family=Open+Sans:wght@400;700&family=Exo+2:wght@400&display=swap">
<style>
  :root {
    --brand-blue: #2a6aa4;
    --brand-blue-dark: #1f5a90;
    --ink-grey: #6b6b6e;
    --rule-grey: #7a7a7a;
    --paper: #ffffff;
    --backdrop: #e9eaec;
  }
  * { box-sizing: border-box; margin: 0; padding: 0; }
  html, body { width: 1200px; height: 900px; overflow: hidden; }
  body { background: var(--backdrop); position: relative; }

  .card {
    position: absolute;
    left: 280px;
    width: 640px;
    height: 366px;
    overflow: hidden;
    box-shadow: 0 6px 18px rgba(0,0,0,0.18);
  }

  /* Front */
  .card--front { top: 56px; background: var(--brand-blue); color: var(--paper); }
  .front__mark {
    position: absolute; left: 50%; top: 78px; transform: translateX(-50%);
    width: 96px; height: 96px; border-radius: 50%; background: var(--paper);
  }
  .front__name {
    position: absolute; left: 0; right: 0; top: 190px; text-align: center;
    font-family: "Roboto", sans-serif; font-weight: 900; font-size: 52px;
    letter-spacing: 0.5px; color: var(--paper);
  }
  .front__services {
    position: absolute; left: 0; right: 0; top: 272px; text-align: center;
    font-family: "Exo 2", sans-serif; font-size: 20px; letter-spacing: 1.5px;
    color: var(--paper);
  }

  /* Back */
  .card--back { top: 478px; background: var(--paper); }
  .back__mark {
    position: absolute; left: 430px; top: 40px;
    width: 130px; height: 120px; border-radius: 50%; background: var(--brand-blue);
  }
  .back__brand {
    position: absolute; right: 36px; top: 168px;
    font-family: "Roboto", sans-serif; font-weight: 900; font-size: 50px;
    color: var(--ink-grey); letter-spacing: 0.5px;
  }
  .back__person { position: absolute; left: 52px; top: 140px; }
  .back__name {
    font-family: "Open Sans", sans-serif; font-weight: 700; font-size: 26px;
    color: var(--brand-blue-dark); line-height: 1.1;
  }
  .back__title {
    font-family: "Open Sans", sans-serif; font-size: 17px; color: var(--ink-grey);
  }
  .back__rule {
    position: absolute; left: 48px; right: 36px; top: 232px;
    height: 2px; background: var(--rule-grey);
  }
  .contact {
    position: absolute; list-style: none;
    font-family: "Exo 2", sans-serif; font-size: 17px; color: var(--ink-grey);
  }
  .contact li { display: flex; align-items: center; gap: 10px; height: 24px; }
  .contact svg { width: 18px; height: 18px; fill: var(--brand-blue-dark); flex: none; }
  .contact--web { left: 46px; top: 246px; }
  .contact--phone { right: 40px; top: 264px; }
  .back__band {
    position: absolute; left: 0; right: 0; bottom: 0; height: 16px;
    background: var(--brand-blue);
  }
</style>
</head>
<body>

<section class="card card--front" aria-label="Card front">
  <div class="front__mark"></div>
  <div class="front__name">LUMO4KART</div>
  <div class="front__services">EFTPOS | ONLINE | MOBILE</div>
</section>

<section class="card card--back" aria-label="Card back">
  <div class="back__mark"></div>
  <div class="back__brand">LUMO4KART</div>

  <div class="back__person">
    <div class="back__name">YOUR NAME</div>
    <div class="back__title">Your Title</div>
  </div>

  <div class="back__rule"></div>

  <ul class="contact contact--web">
    <li>
      <svg viewBox="0 0 20 20" aria-hidden="true"><path d="M1 4h18v12H1z M2 5l8 6 8-6" fill="none" stroke="#1f5a90" stroke-width="1.6"/><path d="M2 5h16l-8 6z"/></svg>
      contact@lumo4kart.com.au
    </li>
    <li>
      <svg viewBox="0 0 20 20" aria-hidden="true"><circle cx="10" cy="10" r="9"/><path d="M1 10h18M10 1c-4 4-4 14 0 18M10 1c4 4 4 14 0 18" fill="none" stroke="#fff" stroke-width="1.2"/></svg>
      lumo4kart.com.au
    </li>
  </ul>

  <ul class="contact contact--phone">
    <li>
      <svg viewBox="0 0 20 20" aria-hidden="true"><path d="M4 1l4 4-2 3c1 3 3 5 6 6l3-2 4 4-3 3C9 19 1 11 1 4z"/></svg>
      0432 587 904
    </li>
    <li>
      <svg viewBox="0 0 20 20" aria-hidden="true"><path d="M5 1h10v18H5z M7 3v12h6V3z" fill-rule="evenodd"/><circle cx="10" cy="17" r="0.9" fill="#fff"/></svg>
      02 6815 3927
    </li>
  </ul>

  <div class="back__band"></div>
</section>

</body>
</html>
```